Golf Course Membership Flyer

I am looking for a design for a double sided A5 flyer that will promote a variety of membership types that are playable either by weekly, fortnightly or monthly instillments. there are packages available from juniors to seniors and they cover playing once a week to 7 days per week. There is something for everyone. We would like to see the image attached used. Our website is www.tanglewoodlinks.com.au
Updates

GuysI have updated some copy and membership details now and am adding some additional photos of the club i.e course, restaurant, changing rooms pro shop etc Added Tuesday, May 30, 2017

Target Market(s)

Primarily male but covers youth and female, regular golfers in Victoria Australia

Industry/Entity Type

Golf Course

Font styles to use
Sans Serif

Colors
acd036
faa54b
0592cd

Requirements
Must have
• Double sided A5. With Logo. (we will provide later.) must have ability to list multiple membership types. We are an award winning 18 hole golf course. we have just been voted 15th best value course in australia.
• see some other work we have had done http://tanglewood.sunnyfairway.com.au/
Nice to have
• A table showing membership inclusions by membership type. The following text: New Golf Membership Passes
• The Prancing Heron is proud to launch its new 2017/18 golf membership pass. You can now enjoy golf all year round, at one of Australia’s leading courses and choose from a variety of pass options that suit every budget. The Prancing Heron boasts private club quality amenities yet remains a public course open to all and one where every visitor feels truly at home.
• For a tour, application form or to find out more call our membership co-ordinator on 03 9482 6150

```html
<!DOCTYPE html>
<html lang="en">
<head>
<meta charset="utf-8">
<title>Prancing Heron Golf Course – New Golf Membership Passes</title>
<link rel="stylesheet" href="https://fonts.googleapis.com/css2?family=Open+Sans:wght@400;700;800&family=Oswald:wght@500;600&display=swap">
<style>
  :root {
    --field: #0f7a3e;
    --row-dark: #107a3f;
    --row-light: #33b34f;
    --rule: #8cc63f;
    --tick: #a9d13c;
    --ink: #ffffff;
  }
  * { box-sizing: border-box; margin: 0; padding: 0; }
  html, body { width: 1200px; height: 847px; overflow: hidden; }
  body { background: var(--field); font-family: "Open Sans", Arial, sans-serif; color: var(--ink); position: relative; }
  .membership-table {
    position: absolute; left: 73px; top: 99px; width: 1055px;
    border-collapse: collapse; table-layout: fixed;
  }
  .membership-table td, .membership-table th { border: 2px solid var(--rule); }
  .brand-cell { background: var(--row-dark); position: relative; height: 95px; }
  .brand-name {
    position: absolute; left: 10px; top: 52px; width: 160px;
    font-weight: 800; font-size: 14px; line-height: 17px; text-align: center; letter-spacing: .1px;
  }
  .brand-mark {
    position: absolute; left: 118px; top: 12px; width: 34px; height: 34px;
    border-radius: 50%; background: var(--ink);
  }
  .headline {
    position: absolute; left: 225px; top: 12px;
    font-family: "Oswald", "Arial Narrow", sans-serif; font-weight: 600;
    font-size: 25px; line-height: 26px;
  }
  .price { background: var(--row-dark); height: 32px; font-weight: 700; font-size: 15px; text-align: center; }
  .pass-name {
    background: var(--row-light); height: 63px; vertical-align: top; padding-top: 6px;
    font-family: "Oswald", "Arial Narrow", sans-serif; font-weight: 500;
    font-size: 15px; line-height: 16px; text-align: center; text-transform: uppercase;
  }
  .feature-row td { height: 25px; }
  .feature-row.tall td { height: 39px; }
  .feature-row.dark { background: var(--row-dark); }
  .feature-row.light { background: var(--row-light); }
  .feature-label { font-size: 14px; line-height: 14px; padding-left: 14px; }
  .check { text-align: center; vertical-align: middle; }
  .check svg { width: 21px; height: 16px; display: block; margin: 0 auto; }
</style>
</head>
<body>
<svg width="0" height="0" style="position:absolute" aria-hidden="true">
  <defs>
    <symbol id="tick" viewBox="0 0 21 16">
      <path d="M1 8.5 L4.5 5 L8.5 9 L16.5 1 L20 4.5 L8.5 15.5 Z" fill="#a9d13c"/>
    </symbol>
  </defs>
</svg>

<table class="membership-table">
  <colgroup>
    <col style="width:360px"><col style="width:105px"><col style="width:84px"><col style="width:84px">
    <col style="width:84px"><col style="width:85px"><col style="width:84px"><col style="width:84px"><col style="width:85px">
  </colgroup>
  <thead>
    <tr>
      <th class="brand-cell" rowspan="2">
        <span class="brand-mark"></span>
        <span class="brand-name">PRANCING HERON<br>GOLF COURSE</span>
        <span class="headline">New Golf<br>Membership<br>Passes</span>
      </th>
      <th class="price">$2540</th><th class="price">$1500</th><th class="price">$900</th><th class="price">$610</th>
      <th class="price">$600</th><th class="price">$500</th><th class="price">$450</th><th class="price">$100</th>
    </tr>
    <tr>
      <th class="pass-name">Platinum<br>Pass</th><th class="pass-name">7 Day<br>Pass</th>
      <th class="pass-name">5 Day<br>Pass</th><th class="pass-name">5 Day<br>S&amp;P Pass</th>
      <th class="pass-name">Afternoon<br>Pass</th><th class="pass-name">1 Day a<br>Week Pass</th>
      <th class="pass-name">Kids<br>Pass</th><th class="pass-name">School<br>Holiday<br>Pass</th>
    </tr>
  </thead>
  <tbody>
    <tr class="feature-row dark"><td class="feature-label">Unrestricted 7 days a Week Access</td>
      <td class="check"><svg><use href="#tick"/></svg></td><td class="check"><svg><use href="#tick"/></svg></td><td></td><td></td><td></td><td></td><td></td><td></td></tr>
    <tr class="feature-row light tall"><td class="feature-label">Unrestricted Monday to Friday Access<br>(excludes Public Holiday)</td>
      <td></td><td></td><td class="check"><svg><use href="#tick"/></svg></td><td class="check"><svg><use href="#tick"/></svg></td><td></td><td></td><td></td><td></td></tr>
    <tr class="feature-row dark"><td class="feature-label">Restricted Monday to Friday Access</td>
      <td></td><td></td><td></td><td></td><td class="check"><svg><use href="#tick"/></svg></td><td class="check"><svg><use href="#tick"/></svg></td><td class="check"><svg><use href="#tick"/></svg></td><td class="check"><svg><use href="#tick"/></svg></td></tr>
    <tr class="feature-row light"><td class="feature-label">Nominated Day Access - Monday to Friday</td>
      <td></td><td></td><td></td><td></td><td></td><td class="check"><svg><use href="#tick"/></svg></td><td></td><td></td></tr>
    <tr class="feature-row dark"><td class="feature-label">Restricted Time Access</td>
      <td></td><td></td><td></td><td></td><td class="check"><svg><use href="#tick"/></svg></td><td></td><td class="check"><svg><use href="#tick"/></svg></td><td></td></tr>
    <tr class="feature-row light tall"><td class="feature-label">Restricted Saturday, Sunday and<br>Public Holiday Access</td>
      <td></td><td></td><td></td><td></td><td></td><td></td><td class="check"><svg><use href="#tick"/></svg></td><td></td></tr>
    <tr class="feature-row dark"><td class="feature-label">No Saturday, Sunday &amp; Public Holiday Access</td>
      <td></td><td></td><td class="check"><svg><use href="#tick"/></svg></td><td class="check"><svg><use href="#tick"/></svg></td><td class="check"><svg><use href="#tick"/></svg></td><td class="check"><svg><use href="#tick"/></svg></td><td></td><td class="check"><svg><use href="#tick"/></svg></td></tr>
    <tr class="feature-row light"><td class="feature-label">Prancing Heron Golf Course Cap</td>
      <td></td><td></td><td></td><td></td><td></td><td></td><td class="check"><svg><use href="#tick"/></svg></td><td class="check"><svg><use href="#tick"/></svg></td></tr>
    <tr class="feature-row dark"><td class="feature-label">Sleeve of Golf Balls</td>
      <td></td><td></td><td></td><td></td><td></td><td></td><td class="check"><svg><use href="#tick"/></svg></td><td></td></tr>
    <tr class="feature-row light"><td class="feature-label">Free Meal on Birthday</td>
      <td></td><td></td><td></td><td></td><td></td><td></td><td class="check"><svg><use href="#tick"/></svg></td><td></td></tr>
    <tr class="feature-row dark"><td class="feature-label">Bring a Friend for $5/Game</td>
      <td></td><td></td><td></td><td></td><td></td><td></td><td class="check"><svg><use href="#tick"/></svg></td><td></td></tr>
    <tr class="feature-row light"><td class="feature-label">50% Discount For Guardian</td>
      <td></td><td></td><td></td><td></td><td></td><td></td><td class="check"><svg><use href="#tick"/></svg></td><td></td></tr>
    <tr class="feature-row dark"><td class="feature-label">Invitations to Play in Kids Competitions</td>
      <td></td><td></td><td></td><td></td><td></td><td></td><td class="check"><svg><use href="#tick"/></svg></td><td></td></tr>
    <tr class="feature-row light"><td class="feature-label">Mates Vouchers</td>
      <td class="check"><svg><use href="#tick"/></svg></td><td></td><td></td><td></td><td></td><td></td><td></td><td></td></tr>
    <tr class="feature-row dark"><td class="feature-label">10% Discount for Pass Holders When Golfing</td>
      <td class="check"><svg><use href="#tick"/></svg></td><td></td><td></td><td></td><td></td><td></td><td></td><td></td></tr>
    <tr class="feature-row light"><td class="feature-label">Children Play For Free</td>
      <td class="check"><svg><use href="#tick"/></svg></td><td></td><td></td><td></td><td></td><td></td><td></td><td></td></tr>
    <tr class="feature-row dark"><td class="feature-label">Golf Shop Benefits</td>
      <td class="check"><svg><use href="#tick"/></svg></td><td></td><td></td><td></td><td></td><td></td><td></td><td></td></tr>
    <tr class="feature-row light"><td class="feature-label">Weekly Payments Via Direct Debit</td>
      <td class="check"><svg><use href="#tick"/></svg></td><td class="check"><svg><use href="#tick"/></svg></td><td class="check"><svg><use href="#tick"/></svg></td><td class="check"><svg><use href="#tick"/></svg></td><td class="check"><svg><use href="#tick"/></svg></td><td class="check"><svg><use href="#tick"/></svg></td><td></td><td class="check"><svg><use href="#tick"/></svg></td></tr>
    <tr class="feature-row dark"><td class="feature-label">Fortnightly Payments Via Direct Debit</td>
      <td class="check"><svg><use href="#tick"/></svg></td><td class="check"><svg><use href="#tick"/></svg></td><td class="check"><svg><use href="#tick"/></svg></td><td class="check"><svg><use href="#tick"/></svg></td><td class="check"><svg><use href="#tick"/></svg></td><td class="check"><svg><use href="#tick"/></svg></td><td></td><td class="check"><svg><use href="#tick"/></svg></td></tr>
    <tr class="feature-row light"><td class="feature-label">Monthly Payments Via Direct Debit</td>
      <td class="check"><svg><use href="#tick"/></svg></td><td class="check"><svg><use href="#tick"/></svg></td><td class="check"><svg><use href="#tick"/></svg></td><td class="check"><svg><use href="#tick"/></svg></td><td class="check"><svg><use href="#tick"/></svg></td><td class="check"><svg><use href="#tick"/></svg></td><td></td><td class="check"><svg><use href="#tick"/></svg></td></tr>
    <tr class="feature-row dark"><td class="feature-label">Quarterly Payments</td>
      <td class="check"><svg><use href="#tick"/></svg></td><td class="check"><svg><use href="#tick"/></svg></td><td></td><td></td><td></td><td></td><td></td><td></td></tr>
    <tr class="feature-row light"><td class="feature-label">Payments in Full</td>
      <td class="check"><svg><use href="#tick"/></svg></td><td class="check"><svg><use href="#tick"/></svg></td><td class="check"><svg><use href="#tick"/></svg></td><td class="check"><svg><use href="#tick"/></svg></td><td class="check"><svg><use href="#tick"/></svg></td><td class="check"><svg><use href="#tick"/></svg></td><td class="check"><svg><use href="#tick"/></svg></td><td class="check"><svg><use href="#tick"/></svg></td></tr>
  </tbody>
</table>
</body>
</html>
```